Wine label for new boutique South African wine focused on the USA market.

Wine label required for new ethical south African red wine called PLUMB which stands for 'Marlowe, tolland, brightly and you' but is also a play on 'SA' and that it has a story to tell. Gerald Marlowe is the wine maker, Tolland the farm owner, and Brightly an investor.

Concept is a simple old type writer font on a white/off white label. Front label would say 'Plumb No.1, 2010 Shiraz, South Africa' and similarly a second for another wine 'Plumb No.2, 2010 Cab/Merlot Blend. Maybe the round stain of the bottom of a wine bottle in the bottom corner? Would also like for the 'plumb' to double up as the logo and work in the form of a stamp.

The rear label will need to tell a short story and be able to accommodate the usual boilerplate info. The story will go something like, ' Plumb No.1: It's a long story, but in short we love our wine and we think you will too. The cooling see breezes of the Indian Ocean help define this world class Shiraz from the Western Cape. Aged in french oak for 20 months, the bold flavors will compliment all red meats or simply enjoy on its own. Learn more about our story at www.plumbvintners.example.

The cab/merlot will read similar: Plumb No.2: It's a long story, but in short we love our wine and we think you will too. The cooling see breezes of the Indian Ocean help define this world class red blend from the Western Cape. Aged in french oak for 20 months, this wine will compliment all red meats or simply enjoy on its own. Learn more about our story at www.plumbvintners.example.

Reason: Had some great designs already, but as i get to understand how ArtBazaarly works, I'm keen to explore as many ideas as possible. Neil

Thanks for all the great designs everybody!

We will make a tough decision in the next couple of days.

Regards

Neil

Target Market(s)

Middle class with some wine knowledge. Price point around $20 -30

Industry/Entity Type

Boutique

Requirements
Nice to have
• A small nod to the wine coming from south Africa in the design would be nice but nothing to over the top
Should not have
• Simple and clear font with plenty of empty space on the label

```html
<!DOCTYPE html>
<html lang="en">
<head>
<meta charset="utf-8">
<title>Plumb No.2 – Wine Label</title>
<link rel="stylesheet" href="https://fonts.googleapis.com/css2?family=Courier+Prime:wght@400;700&family=EB+Garamond:wght@400&display=swap">
<style>
  :root {
    --page: #f2f3d9;
    --frame: #a2289a;
    --linen: #ebe6d8;
    --plum-deep: #5a1550;
    --plum: #8c1f84;
    --plum-light: #a43aa6;
    --sun: #eecd5f;
    --region: #d6d2ab;
    --stamp: #a62a98;
    --stamp-ring: #d9a4d6;
  }
  * { box-sizing: border-box; margin: 0; padding: 0; }
  html, body { width: 800px; height: 1200px; overflow: hidden; }
  body { background: var(--page); position: relative; }

  .label {
    position: absolute;
    left: 39px; top: 37px;
    width: 722px; height: 1124px;
    border: 9px solid var(--frame);
    background: var(--linen);
  }
  .label > * { position: absolute; }

  .sun-emblem {
    left: 289px; top: 45px;
    width: 126px; height: 126px;
    border-radius: 50%;
    background: linear-gradient(to bottom, var(--sun) 0 60%, #e9c552 60% 100%);
    box-shadow: 0 0 0 2px #6b6248;
  }

  .wine-name, .wine-number {
    left: 0; width: 100%;
    text-align: center;
    font-family: "Courier Prime", "Courier New", monospace;
    font-weight: 700;
    color: var(--plum-deep);
    text-shadow: 1px 1px 0 #c98fc2, -1px -1px 0 #2e0a29, 2px 3px 3px rgba(0,0,0,0.25);
  }
  .wine-name {
    top: 196px;
    font-size: 104px;
    letter-spacing: 8px;
    line-height: 1;
  }
  .wine-number {
    top: 330px;
    font-size: 86px;
    line-height: 1;
  }

  .vintage, .varietal, .style {
    left: 0; width: 100%;
    text-align: center;
    font-family: "Courier Prime", "Courier New", monospace;
    font-weight: 400;
    line-height: 1;
  }
  .vintage  { top: 543px; font-size: 42px; color: var(--plum); }
  .varietal { top: 611px; font-size: 43px; color: var(--plum); }
  .style    { top: 661px; font-size: 43px; color: var(--plum-light); }

  .region-map {
    left: 98px; top: 710px;
    width: 550px; height: 320px;
    background: var(--region);
    border-radius: 18% 32% 46% 40% / 14% 28% 66% 58%;
    opacity: 0.85;
  }

  .origin {
    left: 0; width: 100%;
    top: 846px;
    text-align: center;
    font-family: "EB Garamond", Georgia, serif;
    font-size: 47px;
    color: var(--plum);
  }

  .maker-stamp {
    left: 498px; top: 986px;
    width: 190px; height: 110px;
  }
  .maker-stamp .stamp-ring {
    position: absolute;
    left: 44px; top: 0;
    width: 106px; height: 106px;
    border-radius: 50%;
    border: 3px solid var(--stamp-ring);
  }
  .maker-stamp .stamp-name {
    position: absolute;
    left: 0; top: 30px; width: 100%;
    text-align: center;
    font-family: "Courier Prime", "Courier New", monospace;
    font-weight: 700;
    font-size: 46px;
    color: var(--stamp);
  }
</style>
</head>
<body>
  <main class="label">
    <div class="sun-emblem" role="img" aria-label="Setting sun emblem"></div>
    <h1 class="wine-name">PLUMB</h1>
    <p class="wine-number">No.2</p>
    <p class="vintage">2012</p>
    <p class="varietal">Cab/Merlot</p>
    <p class="style">Blend</p>
    <div class="region-map" role="img" aria-label="Faint map of the southern tip of South Africa"></div>
    <p class="origin">South Africa</p>
    <div class="maker-stamp">
      <span class="stamp-ring"></span>
      <span class="stamp-name">PLUMB</span>
    </div>
  </main>
</body>
</html>
```